Flyer for Weightlifting Sports Club

We need a flyer to explain what weightlifting is and attract people of ages between 10 and 15 years old, so that they are encouraged to practice this sport with us. It should also serve to convince parents that it is a safe sport for children. We would like it to have an informal look, with the indispensable text and with many attractive graphics, even a comic type format. It could include the message that adults are also invited to try it. An invitation to try out for a week presenting the flyer should be visible.

Target Market(s)

Children from 10 to 15 years old

Font styles to use
Decorative
Script

Colors
b768aa
33a6d7
cadf82
f59296
f9ba93
faa54b

Requirements
Must have
• Information about our sport Drawings or pictures of child weightlifting

```html
<!DOCTYPE html>
<html lang="es">
<head>
<meta charset="utf-8">
<title>La Halterofilia – Club Deportivo Pesas Giralda</title>
<link rel="stylesheet" href="https://fonts.googleapis.com/css2?family=Kaushan+Script&family=Kalam:wght@700&family=Noto+Sans:wght@700&display=swap">
<style>
  :root {
    --ink: #1b1552;
    --teal: #4eb3cc;
    --teal-soft: #bfe3ec;
    --orange: #f39a1e;
    --orange-line: #f08a3c;
    --pink: #f2a0ab;
    --white: #ffffff;
    --frame: #e4e7ee;
  }
  * { margin: 0; padding: 0; box-sizing: border-box; }
  html, body { width: 913px; height: 1200px; overflow: hidden; background: var(--white); }
  .flyer { position: relative; width: 913px; height: 1200px; overflow: hidden; color: var(--ink); }

  .header-band {
    position: absolute; left: 340px; top: 0; width: 498px; height: 148px;
    background: linear-gradient(90deg, rgba(255,255,255,0) 0%, var(--teal-soft) 45%, var(--teal) 100%);
  }
  .header-rule { position: absolute; left: 410px; top: 147px; width: 428px; height: 12px;
    background: linear-gradient(90deg, #f9c9a0, var(--orange-line)); }
  .title {
    position: absolute; left: 424px; top: 62px;
    font: 400 56px/1 "Kaushan Script", cursive; color: var(--ink);
  }
  .title-icon { position: absolute; left: 357px; top: 38px; width: 58px; height: 88px; }

  .hex { position: absolute; }

  .copy { position: absolute; font-family: "Kalam", cursive; font-weight: 700; color: var(--ink); }
  .copy .line { position: absolute; white-space: nowrap; line-height: 1.2;
    text-align: justify; text-align-last: justify; }
  .copy .line.last { text-align-last: left; }
  .copy--main { font-size: 16px; }
  .copy--small { font-size: 14px; }

  .lead-in { position: absolute; left: 372px; top: 750px;
    font: 700 31px/1.2 "Kalam", cursive; color: var(--ink); }

  .dumbbell { position: absolute; left: 138px; top: 680px; width: 162px; height: 104px; }

  .club-band {
    position: absolute; left: 0; top: 818px; width: 838px; height: 380px;
    background: linear-gradient(90deg, #ffffff 0%, #e6f4f8 35%, var(--teal-soft) 60%, var(--teal) 100%);
  }
  .club-name {
    position: absolute; left: 40px; top: 848px; width: 520px; text-align: center;
    font: 400 48px/60px "Kaushan Script", cursive; color: var(--ink);
  }
  .invite {
    position: absolute; left: 80px; top: 994px; width: 450px; text-align: center;
    font: 700 23px/30px "Noto Sans", sans-serif; color: var(--ink);
  }
  .trial {
    position: absolute; left: 80px; top: 1094px; width: 450px; text-align: center;
    font: 700 15px/22px "Noto Sans", sans-serif; color: var(--orange-line);
  }
  .contact {
    position: absolute; left: 88px; top: 1130px; width: 420px; height: 68px;
    background: linear-gradient(90deg, var(--pink), rgba(255,255,255,0.4));
    padding-top: 13px; padding-left: 28px; font-style: normal;
    font: 700 16.5px/22px "Noto Sans", sans-serif; color: var(--ink);
  }
  .fees {
    position: absolute; left: 520px; top: 833px; width: 318px; height: 355px;
    background: var(--orange); border-radius: 18px;
    color: var(--white); font: 700 20px/25px "Noto Sans", sans-serif;
    padding: 20px 0 0 23px;
  }
  .fees h2 { font: inherit; font-size: 22px; text-align: center; margin: 0 0 26px -23px; }
  .fees p + p { margin-top: 25px; }
</style>
</head>
<body>
<main class="flyer">
  <div class="header-band"></div>
  <div class="header-rule"></div>
  <svg class="title-icon" viewBox="0 0 58 88" role="img" aria-label="Pictograma de levantador con barra">
    <rect x="0" y="0" width="58" height="88" rx="8" fill="#3a3478" opacity="0.85"/>
  </svg>
  <h1 class="title">La Halterofilia</h1>

  <svg class="hex" style="left:103px;top:66px" width="314" height="342" viewBox="0 0 314 342">
    <defs><linearGradient id="ph1" x1="0" y1="0" x2="1" y2="1">
      <stop offset="0" stop-color="#c9cfe0"/><stop offset="0.5" stop-color="#c4464a"/><stop offset="1" stop-color="#d9c9b8"/></linearGradient></defs>
    <polygon points="157,2 312,86 312,256 157,340 2,256 2,86" fill="var(--frame)"/>
    <polygon points="157,14 300,93 300,249 157,328 14,249 14,93" fill="url(#ph1)" role="img" aria-label="Foto de una joven halterófila en sentadilla con la barra sobre la cabeza"/>
  </svg>

  <svg class="hex" style="left:112px;top:420px" width="204" height="250" viewBox="0 0 204 250">
    <defs><linearGradient id="ph2" x1="0" y1="0" x2="1" y2="1">
      <stop offset="0" stop-color="#d8cfc8"/><stop offset="0.5" stop-color="#c0334a"/><stop offset="1" stop-color="#3a3a4a"/></linearGradient></defs>
    <polygon points="102,2 202,60 202,190 102,248 2,190 2,60" fill="var(--frame)"/>
    <polygon points="102,14 191,66 191,184 102,236 13,184 13,66" fill="url(#ph2)" role="img" aria-label="Foto de un niño levantando una barra en competición"/>
  </svg>

  <svg class="hex" style="left:603px;top:590px" width="218" height="220" viewBox="0 0 218 220">
    <defs><linearGradient id="ph3" x1="0" y1="0" x2="1" y2="1">
      <stop offset="0" stop-color="#2d5fa8"/><stop offset="0.5" stop-color="#1f3e7a"/><stop offset="1" stop-color="#c8344a"/></linearGradient></defs>
    <polygon points="109,2 216,55 216,165 109,218 2,165 2,55" fill="var(--frame)"/>
    <polygon points="109,12 206,61 206,159 109,208 12,159 12,61" fill="url(#ph3)" role="img" aria-label="Foto de un halterófilo adulto levantando una barra con discos rojos"/>
  </svg>

  <section class="copy copy--main">
    <div class="line" style="left:424px;top:174px;width:378px">La halterofilia o levantamiento de pesas es un</div>
    <div class="line" style="left:424px;top:202px;width:378px">deporte olímpico que se practica desde la</div>
    <div class="line" style="left:424px;top:229px;width:378px">antigüedad, y que llega a nuestros días como una</div>
    <div class="line" style="left:424px;top:257px;width:378px">actividad física que combina la fuerza, la</div>
    <div class="line" style="left:424px;top:284px;width:378px">velocidad, la agilidad y la técnica. Todo esto unido</div>
    <div class="line" style="left:424px;top:312px;width:378px">a la carga progresiva teniendo siempre en cuenta</div>
    <div class="line" style="left:416px;top:339px;width:386px">las posibilidades de cada persona, hace que sea</div>
    <div class="line last" style="left:370px;top:367px">muy beneficiosa su práctica a cualquier edad.</div>

    <div class="line" style="left:278px;top:422px;width:524px">En la infancia desarrolla la fuerza, corrige problemas posturales,</div>
    <div class="line" style="left:313px;top:449px;width:489px">estimula el crecimiento y mejora la coordinación y el</div>
    <div class="line last" style="left:333px;top:476px">rendimiento intelectual.</div>
    <div class="line" style="left:333px;top:504px;width:469px">En las personas adultas, además, favorece el aumento de la</div>
    <div class="line" style="left:333px;top:531px;width:469px">masa muscular, mejora el sistema cardiovascular, ayuda en la</div>
    <div class="line last" style="left:333px;top:558px">pérdida de grasa y aumenta la densidad ósea.</div>
  </section>

  <section class="copy copy--small">
    <div class="line" style="left:305px;top:624px;width:292px">Este deporte es muy inclusivo, ya que en</div>
    <div class="line" style="left:305px;top:648px;width:292px">las competiciones se tienen en cuenta el</div>
    <div class="line" style="left:305px;top:672px;width:292px">género, la edad y el peso corporal de los y</div>
    <div class="line last" style="left:305px;top:696px">las levantadoras.</div>
  </section>

  <svg class="dumbbell" viewBox="0 0 162 104" role="img" aria-label="Ilustración de una mancuerna">
    <rect x="0" y="0" width="162" height="104" rx="14" fill="#3d3d3d" opacity="0.8"/>
  </svg>

  <p class="lead-in">Por eso el</p>

  <div class="club-band"></div>
  <h2 class="club-name">Club Deportivo<br>Pesas Giralda</h2>
  <p class="invite">Te invita a que te animes<br>para que te inscribas..!<br>niños adultos y adolecentes</p>
  <p class="trial">¡Presenta este folleto y prueba una semana gratis!</p>

  <aside class="fees">
    <h2>Nuestras cuotas:</h2>
    <p>15€/mes para menores<br>de 18 años.<br>25€/mes para mayores<br>de 18 años.<br>Tres sesiones semanales<br>de 60 minutos.</p>
    <p>Horarios:<br>De lunes a viernes de<br>17:00 a 20:30</p>
  </aside>

  <address class="contact">
    C/. Jardín de la Fragua, s/n. 41010-Sevilla<br>
    Teléfono de contacto XXXXXXXXX. Luis
  </address>
</main>
</body>
</html>
```